Management consulting Company in the electronic payment ecosystem needs a Website

We need to have a "showcase" style website that contains the key message that our company is able to provide management consulting in the world of payment systems. Our mission is to assist our clients in reviewing their sales, purchasing, operation and IT processes and to support them in identifying the best solution in the use of payment systems.

```html
<!DOCTYPE html>
<html lang="en">
<head>
<meta charset="utf-8">
<title>Veridan Consulting – Management Consulting in Payment Systems</title>
<link href="https://fonts.googleapis.com/css2?family=Raleway:wght@400;500;600;700&display=swap" rel="stylesheet">
<style>
:root{
  --navy:#0e1b5e;
  --navy-deep:#0a1246;
  --ink:#0b1033;
  --accent:#2a3b9a;
  --text:#333a4d;
  --muted:#7a8093;
  --page:#f7f7f9;
  --white:#ffffff;
  --line:#e3e5ec;
}
*{box-sizing:border-box;margin:0;padding:0}
html,body{width:1200px;height:4747px;overflow:hidden}
body{font-family:'Raleway',sans-serif;color:var(--text);background:var(--page)}
.canvas{position:relative;width:1200px;height:4747px;overflow:hidden;background:var(--page)}
.abs{position:absolute}

/* header */
.site-header{left:0;top:0;width:1200px;height:87px;background:var(--white)}
.brand{display:flex;align-items:center;gap:10px}
.brand-dot{width:46px;height:46px;border-radius:50%;border:6px solid var(--navy)}
.brand-name{font-weight:700;font-size:34px;color:var(--navy);letter-spacing:.5px}
.site-header .brand{position:absolute;left:149px;top:20px}
.nav{position:absolute;left:550px;top:36px;display:flex;gap:38px;font-size:14px;font-weight:500;color:var(--text)}
.btn-contact{position:absolute;left:929px;top:26px;width:120px;height:42px;border-radius:4px;background:var(--navy);color:#fff;font-size:13px;font-weight:600;display:flex;align-items:center;justify-content:center}

/* hero */
.hero{left:0;top:87px;width:1200px;height:660px;background:linear-gradient(100deg,#3a4a78 0%,#6b7796 35%,#9aa0ae 55%,#5f6d8e 80%,#2e3c6c 100%)}
.hero-shade{left:0;top:87px;width:1200px;height:660px;background:linear-gradient(90deg,rgba(14,27,94,.55),rgba(14,27,94,.15) 60%,rgba(14,27,94,.3))}
.hero-title{left:149px;top:352px;color:#fff;font-size:37px;font-weight:600}
.hero-sub{left:149px;top:403px;color:#fff;font-size:28px;font-weight:400}
.hero-text{left:149px;top:458px;width:490px;color:#fff;font-size:15px;line-height:26px}
.btn-dark{background:var(--navy);color:#fff;font-size:14px;font-weight:500;display:flex;align-items:center;gap:22px;padding-left:28px}
.hero-btn{left:151px;top:544px;width:220px;height:43px}
.slide-dot{left:1080px;top:370px;width:22px;height:22px;border-radius:50%;border:2px solid #fff;background:var(--navy)}

/* section titles */
.section-title{left:0;width:1200px;text-align:center;font-size:35px;color:var(--navy-deep)}

/* services */
.services-title{top:800px;font-weight:400}
.services-title b{font-weight:700;color:var(--navy)}
.service-card{width:404px;height:157px;background:#fff;box-shadow:0 4px 14px rgba(20,30,80,.12);overflow:hidden}
.service-card.active{background:var(--navy);color:#fff}
.service-icon{position:absolute;left:24px;top:42px;width:58px;height:58px;border:2px solid var(--navy);border-radius:10px}
.service-card.active .service-icon{border-color:#fff}
.service-card h3{position:absolute;left:100px;top:38px;font-size:15px;font-weight:600;color:var(--navy)}
.service-card.active h3{color:#fff}
.service-card p{position:absolute;left:100px;top:68px;width:280px;font-size:12.5px;line-height:20px;color:var(--text)}
.service-card.active p{color:#dfe3f5}
.card-corner{position:absolute;right:0;bottom:0;width:52px;height:32px;border-top-left-radius:32px;background:#8c93ad;display:flex;align-items:center;justify-content:center}

/* welcome */
.welcome-photo{left:210px;top:1314px;width:391px;height:424px;background:linear-gradient(120deg,#7c6a5c,#b7a795 45%,#4c5a7a)}
.welcome-box{left:601px;top:1314px;width:448px;height:424px;background:#fff;box-shadow:0 4px 18px rgba(20,30,80,.08)}
.welcome-small{position:absolute;left:48px;top:34px;font-size:22px;color:var(--navy-deep);font-weight:500}
.welcome-big{position:absolute;left:48px;top:68px;font-size:36px;color:var(--navy);font-weight:600}
.welcome-body{position:absolute;left:48px;top:122px;width:360px;font-size:12.5px;line-height:22px}
.welcome-body p{margin-bottom:17px}
.welcome-body p.tight{margin-bottom:6px}
.welcome-btn{position:absolute;left:48px;top:339px;width:169px;height:43px;padding-left:20px;gap:14px;font-size:13px}
.badge{left:149px;top:1664px;width:151px;height:137px;background:var(--navy);color:#fff;text-align:center;padding-top:30px}
.badge strong{display:block;font-size:32px;font-weight:500}
.badge span{font-size:15px}

/* experience */
.experience{left:0;top:1840px;width:1200px;height:820px;background:linear-gradient(180deg,#16236c,#0c1653)}
.exp-ring{left:556px;top:1997px;width:64px;height:64px;border-radius:50%;border:9px solid #fff}
.exp-title{left:0;top:2086px;width:1200px;text-align:center;color:#fff;font-size:35px;font-weight:600}
.exp-rule{left:570px;top:2141px;width:60px;height:3px;background:#fff}
.exp-text{left:200px;top:2168px;width:800px;text-align:center;color:#dfe3f5;font-size:18.5px;line-height:32px}
.stat{width:206px;height:118px;border:1px solid rgba(255,255,255,.28);background:rgba(40,60,150,.35);color:#fff}
.stat-icon{position:absolute;left:22px;top:38px;width:44px;height:42px;border:2px solid #fff;border-radius:50%}
.stat strong{position:absolute;left:78px;top:36px;font-size:28px;font-weight:500}
.stat span{position:absolute;left:78px;top:74px;font-size:13px}
.meeting-photo{left:184px;top:2444px;width:831px;height:439px;background:linear-gradient(110deg,#c9c2b8,#8d8a86 35%,#2e3448 55%,#b6ab9d 80%,#e0d8cc);box-shadow:0 10px 30px rgba(10,20,60,.25)}

/* team */
.team-title{top:2972px;font-weight:600}
.team-card{height:222px;background:#fff;border:1px solid var(--line);box-shadow:0 4px 12px rgba(20,30,80,.06)}
.team-photo{position:absolute;left:0;top:0;height:100%;background:linear-gradient(135deg,#9aa3b5,#c9c3bb 50%,#7d879c)}
.team-info{position:absolute;top:22px;width:200px}
.team-info h4{font-size:13px;font-weight:600;color:var(--ink)}
.team-info .exp{font-size:10.5px;color:var(--muted);margin-top:8px}
.team-info p{font-size:10.5px;line-height:22px;margin-top:6px;color:var(--text)}

/* testimonials */
.clients{left:0;top:3373px;width:1200px;height:479px;background:#f0f0f3}
.clients-title{top:3452px;font-weight:500;color:var(--ink)}
.quote-box{left:276px;top:3594px;width:647px;height:157px;background:#fff}
.avatar{left:562px;top:3524px;width:76px;height:76px;border-radius:50%;background:linear-gradient(135deg,#8d96ab,#cbbfae);border:3px solid #fff}
.quote-mark{position:absolute;left:58px;top:28px;font-size:42px;line-height:1;color:var(--navy);font-weight:700}
.quote-text{position:absolute;left:30px;top:46px;width:587px;text-align:center;font-size:13.5px;line-height:22px}
.quote-name{position:absolute;left:0;top:124px;width:647px;text-align:center;font-size:14px;color:var(--accent);font-weight:500}
.arrow-btn{width:54px;height:54px;border-radius:50%;background:var(--navy);display:flex;align-items:center;justify-content:center}
.dots{left:570px;top:3777px;display:flex;gap:8px}
.dots i{width:14px;height:14px;border-radius:50%;background:#b8bbc6}
.dots i.on{background:var(--navy)}

/* news */
.news-card{width:277px;height:346px;background:#fff;border:1px solid var(--line);box-shadow:0 4px 12px rgba(20,30,80,.06)}
.news-photo{position:absolute;left:0;top:0;width:100%;height:152px;background:linear-gradient(135deg,#d9dbe0,#6b7286 55%,#b9bcc5)}
.news-go{position:absolute;right:0;top:122px;width:32px;height:30px;background:#3c4256;display:flex;align-items:center;justify-content:center}
.news-tag{position:absolute;left:22px;top:184px;font-size:10px;color:var(--muted)}
.news-card h5{position:absolute;left:22px;top:204px;width:230px;font-size:12px;font-weight:600;line-height:16px;color:var(--ink)}
.news-card p{position:absolute;left:22px;top:248px;width:230px;font-size:11.5px;line-height:18px;color:var(--muted)}

/* footer */
.footer{left:0;top:4250px;width:1200px;height:497px;background:var(--ink)}
.footer .brand{position:absolute;left:147px;top:190px}
.footer .brand-dot{border-color:#fff}
.footer .brand-name{color:#fff}
.footer-about{left:152px;top:4512px;width:250px;color:#d5d8e6;font-size:12.5px;line-height:21px}
.socials{left:154px;top:4592px;display:flex;gap:14px}
.socials i{width:34px;height:34px;border-radius:50%;border:2px solid #fff}
.footer-col h6{font-size:15px;font-weight:500;color:#fff;letter-spacing:.3px}
.footer-col ul{list-style:none;margin-top:14px}
.footer-col li{font-size:12.5px;color:#d5d8e6;line-height:25.5px}
.footer-col li::before{content:"›";margin-right:10px}
.contact-line{display:flex;gap:10px;font-size:12.5px;color:#d5d8e6;margin-top:14px;line-height:19px}
.email-input{margin-top:14px;width:210px;height:40px;border:1px solid #fff;color:#d5d8e6;font-size:12.5px;display:flex;align-items:center;justify-content:center}
.subscribe-btn{margin-top:11px;width:210px;height:40px;background:#c8ccef;color:var(--navy);font-size:12.5px;display:flex;align-items:center;gap:60px;padding-left:22px}
.footer-rule{left:0;top:4672px;width:1200px;height:1px;background:rgba(255,255,255,.18)}
.legal{top:4698px;font-size:12.5px;color:#d5d8e6}
</style>
</head>
<body>
<div class="canvas">

  <header class="abs site-header">
    <div class="brand"><span class="brand-dot"></span><span class="brand-name">Veridan</span></div>
    <nav class="nav"><span>HOME</span><span>SERVICES</span><span>NEWS</span><span>OUR TEAM</span></nav>
    <div class="btn-contact">CONTACT</div>
  </header>

  <section>
    <div class="abs hero" role="img" aria-label="Consultants meeting with clients around a tablet in a bright office"></div>
    <div class="abs hero-shade"></div>
    <svg class="abs" style="left:0;top:600px" width="1200" height="160" viewBox="0 600 1200 160">
      <path d="M0 640 Q560 820 1200 640 L1200 760 L0 760 Z" fill="#f7f7f9"/>
      <path d="M0 640 Q560 820 1200 640" fill="none" stroke="#1f2d7a" stroke-width="5"/>
    </svg>
    <h1 class="abs hero-title">MANAGEMENT CONSULTING</h1>
    <div class="abs hero-sub">IN THE WORLD OF PAYMENT SYSTEMS</div>
    <p class="abs hero-text">Lorem Ipsum is simply dummy text of the printing and typesetting industry. Lorem Ipsum has been the industry's standard.</p>
    <div class="abs btn-dark hero-btn">CONSULTATION
      <svg width="26" height="12" viewBox="0 0 26 12"><path d="M0 6H24M19 1l5 5-5 5" stroke="#fff" stroke-width="1.6" fill="none"/></svg>
    </div>
    <div class="abs slide-dot"></div>
  </section>

  <section>
    <h2 class="abs section-title services-title">Our <b>Services</b></h2>
    <div class="abs service-card active" style="left:184px;top:874px">
      <div class="service-icon" role="img" aria-label="Management icon"></div>
      <h3>MANAGEMENT CONSULTING</h3>
      <p>Lorem Ipsum is simply dummy text the printing and typesetting industry. Lorem Ipsum has been the industry's standard</p>
      <div class="card-corner"><svg width="22" height="10"><path d="M0 5H20M16 1l4 4-4 4" stroke="#fff" stroke-width="1.4" fill="none"/></svg></div>
    </div>
    <div class="abs service-card" style="left:612px;top:874px">
      <div class="service-icon" role="img" aria-label="Client support icon"></div>
      <h3>ASSIST OUR CLIENTS</h3>
      <p>Lorem Ipsum is simply dummy text the printing and typesetting industry. Lorem Ipsum has been the industry's standard</p>
      <div class="card-corner"><svg width="22" height="10"><path d="M0 5H20M16 1l4 4-4 4" stroke="#fff" stroke-width="1.4" fill="none"/></svg></div>
    </div>
    <div class="abs service-card" style="left:184px;top:1054px">
      <div class="service-icon" role="img" aria-label="Sales review icon"></div>
      <h3>REVIEWING THEIR SALES,</h3>
      <p>Lorem Ipsum is simply dummy text the printing and typesetting industry. Lorem Ipsum has been the industry's standard</p>
      <div class="card-corner"><svg width="22" height="10"><path d="M0 5H20M16 1l4 4-4 4" stroke="#fff" stroke-width="1.4" fill="none"/></svg></div>
    </div>
    <div class="abs service-card" style="left:612px;top:1054px">
      <div class="service-icon" role="img" aria-label="Payment solutions icon"></div>
      <h3>PAYMENT SOLUTIONS</h3>
      <p>Lorem Ipsum is simply dummy text the printing and typesetting industry. Lorem Ipsum has been the industry's standard</p>
      <div class="card-corner"><svg width="22" height="10"><path d="M0 5H20M16 1l4 4-4 4" stroke="#fff" stroke-width="1.4" fill="none"/></svg></div>
    </div>
  </section>

  <section>
    <div class="abs welcome-photo" role="img" aria-label="Senior client discussing documents with an advisor"></div>
    <div class="abs welcome-box">
      <div class="welcome-small">Welcome to the</div>
      <div class="welcome-big">Veridan Consulting</div>
      <div class="welcome-body">
        <p>Lorem Ipsum is simply dummy text of the printing and typesetting industry. Lorem Ipsum has been the industry's standard dummy text ever since the 1500s,</p>
        <p class="tight">When an unknown printer took a galley of type.</p>
        <p class="tight">It to make a type specimen book.</p>
        <p class="tight">Centuries, but also the leap into electronic.</p>
        <p class="tight">It to make a type specimen book.</p>
      </div>
      <div class="btn-dark welcome-btn">GET A QUOTE
        <svg width="26" height="12" viewBox="0 0 26 12"><path d="M0 6H24M19 1l5 5-5 5" stroke="#fff" stroke-width="1.6" fill="none"/></svg>
      </div>
    </div>
    <div class="abs badge"><strong>1000+</strong><span>Successful</span></div>
  </section>

  <section>
    <div class="abs experience" role="img" aria-label="Dark blue backdrop with a faint scale of justice"></div>
    <svg class="abs" style="left:0;top:1838px" width="1200" height="80" viewBox="0 0 1200 80">
      <path d="M0 0 H1200 V2 Q600 120 0 2 Z" fill="#f7f7f9"/>
    </svg>
    <div class="abs" style="left:0;top:2660px;width:1200px;height:10px;background:var(--page)"></div>
    <div class="abs exp-ring"></div>
    <h2 class="abs exp-title">20 YEARS OF EXPERIENCE IN CONSULTING</h2>
    <div class="abs exp-rule"></div>
    <p class="abs exp-text">Lorem Ipsum is simply dummy text of the printing and typesetting industry. Lorem Ipsum has been the industry's standard dummy text ever since the 1500s,</p>
    <div class="abs stat" style="left:153px;top:2256px"><div class="stat-icon"></div><strong>250+</strong><span>Business Client</span></div>
    <div class="abs stat" style="left:381px;top:2256px"><div class="stat-icon"></div><strong>250+</strong><span>Team Members</span></div>
    <div class="abs stat" style="left:610px;top:2256px"><div class="stat-icon"></div><strong>450+</strong><span>Happy Clients</span></div>
    <div class="abs stat" style="left:840px;top:2256px"><div class="stat-icon"></div><strong>40+</strong><span>Awards Win</span></div>
    <div class="abs meeting-photo" role="img" aria-label="Business partners shaking hands across a meeting table"></div>
  </section>

  <section>
    <h2 class="abs section-title team-title">OUR TEAM</h2>
    <div class="abs team-card" style="left:142px;top:3054px;width:455px">
      <div class="team-photo" style="width:223px" role="img" aria-label="Portrait of team member one"></div>
      <div class="team-info" style="left:254px">
        <h4>Name 1</h4><div class="exp">Experience 10 Years</div>
        <p>Lorem Ipsum is simply dummy text of the printing and typesetting industry. Lorem Ipsum has been the industry's standard dummy text</p>
      </div>
    </div>
    <div class="abs team-card" style="left:612px;top:3054px;width:450px;height:218px">
      <div class="team-photo" style="width:217px" role="img" aria-label="Portrait of team member two"></div>
      <div class="team-info" style="left:252px">
        <h4>Name 2</h4><div class="exp">Experience 10 Years</div>
        <p>Lorem Ipsum is simply dummy text of the printing and typesetting industry. Lorem Ipsum has been the industry's standard dummy text</p>
      </div>
    </div>
  </section>

  <section>
    <div class="abs clients" role="img" aria-label="Light grey backdrop with faint office buildings"></div>
    <h2 class="abs section-title clients-title">WHAT OUR CLIENTS SAID</h2>
    <div class="abs quote-box">
      <div class="quote-mark">“</div>
      <p class="quote-text">Lorem Ipsum is simply dummy text of the printing and typesetting industry. Lorem Ipsum has been the industry's standard dummy text ever since the 1500s, Lorem Ipsum is simply dummy text of the printing and typesetting</p>
      <div class="quote-name">MAREK OLSEN</div>
    </div>
    <div class="abs avatar" role="img" aria-label="Client portrait"></div>
    <div class="abs arrow-btn" style="left:185px;top:3626px"><svg width="12" height="18"><path d="M10 1L2 9l8 8" stroke="#fff" stroke-width="2" fill="none"/></svg></div>
    <div class="abs arrow-btn" style="left:959px;top:3626px"><svg width="12" height="18"><path d="M2 1l8 8-8 8" stroke="#fff" stroke-width="2" fill="none"/></svg></div>
    <div class="abs dots"><i></i><i class="on"></i><i></i></div>
  </section>

  <section>
    <div class="abs news-card" style="left:160px;top:3860px">
      <div class="news-photo" role="img" aria-label="Colleagues working at laptops"></div>
      <div class="news-go"><svg width="14" height="10"><path d="M0 5H12M8 1l4 4-4 4" stroke="#fff" stroke-width="1.3" fill="none"/></svg></div>
      <div class="news-tag">NEWS</div>
      <h5>Lorem Ipsum is simply dummy text of the printing and typesetting</h5>
      <p>Lorem Ipsum is simply dummy text of the printing and typesetting industry. Lorem Ipsum has been the industry's standard dummy</p>
    </div>
    <div class="abs news-card" style="left:461px;top:3860px">
      <div class="news-photo" role="img" aria-label="Video call on a laptop screen"></div>
      <div class="news-go"><svg width="14" height="10"><path d="M0 5H12M8 1l4 4-4 4" stroke="#fff" stroke-width="1.3" fill="none"/></svg></div>
      <div class="news-tag">NEWS</div>
      <h5>Lorem Ipsum is simply dummy text of the printing and typesetting</h5>
      <p>Lorem Ipsum is simply dummy text of the printing and typesetting industry. Lorem Ipsum has been the industry's standard dummy...</p>
    </div>
    <div class="abs news-card" style="left:761px;top:3860px">
      <div class="news-photo" role="img" aria-label="Hands reviewing reports with a tablet"></div>
      <div class="news-go"><svg width="14" height="10"><path d="M0 5H12M8 1l4 4-4 4" stroke="#fff" stroke-width="1.3" fill="none"/></svg></div>
      <div class="news-tag">NEWS</div>
      <h5>Lorem Ipsum is simply dummy text of the printing and typesetting</h5>
      <p>Lorem Ipsum is simply dummy text of the printing and typesetting industry. Lorem Ipsum has been the industry's standard dummy...</p>
    </div>
  </section>

  <footer>
    <div class="abs footer">
      <div class="brand"><span class="brand-dot"></span><span class="brand-name">Veridan</span></div>
    </div>
    <svg class="abs" style="left:0;top:4248px" width="1200" height="90" viewBox="0 0 1200 90">
      <path d="M0 0 H1200 V20 Q600 140 0 20 Z" fill="#f7f7f9"/>
    </svg>
    <p class="abs footer-about">Lorem Ipsum is simply dummy text of the printing and typesetting industry. Lorem Ipsum has been the industry's</p>
    <div class="abs socials"><i></i><i></i><i></i></div>
    <div class="abs footer-col" style="left:439px;top:4450px">
      <h6>USEFUL LINKS</h6>
      <ul><li>Home</li><li>Services</li><li>News</li><li>Our Team</li><li>Contact Us</li></ul>
    </div>
    <div class="abs footer-col" style="left:600px;top:4450px">
      <h6>OFFICE INFO</h6>
      <div class="contact-line"><svg width="16" height="16" viewBox="0 0 24 24"><path d="M6.6 10.8a15 15 0 006.6 6.6l2.2-2.2a1 1 0 011-.25 11.4 11.4 0 003.6.6 1 1 0 011 1V20a1 1 0 01-1 1A17 17 0 013 4a1 1 0 011-1h3.5a1 1 0 011 1c0 1.25.2 2.45.6 3.6a1 1 0 01-.25 1z" fill="#fff"/></svg>+00 123 456 7890</div>
      <div class="contact-line"><svg width="16" height="14" viewBox="0 0 24 20"><rect x="1" y="1" width="22" height="18" fill="#fff"/><path d="M1 1l11 9 11-9" stroke="#0b1033" stroke-width="2" fill="none"/></svg>info@veridan-consulting.com</div>
      <div class="contact-line"><svg width="16" height="18" viewBox="0 0 24 28"><path d="M12 0a9 9 0 00-9 9c0 7 9 19 9 19s9-12 9-19a9 9 0 00-9-9zm0 13a4 4 0 110-8 4 4 0 010 8z" fill="#fff"/></svg><span>Uferweg 12 - 78462<br>Lindenbach</span></div>
    </div>
    <div class="abs footer-col" style="left:838px;top:4450px">
      <h6>SUBSCRIBE NOW</h6>
      <div class="email-input">Enter email Address</div>
      <div class="subscribe-btn">SUBSCRIBE NOW
        <svg width="22" height="12" viewBox="0 0 26 12"><path d="M0 6H24M19 1l5 5-5 5" stroke="#0e1b5e" stroke-width="1.6" fill="none"/></svg>
      </div>
    </div>
    <div class="abs footer-rule"></div>
    <div class="abs legal" style="left:150px">Copyright © 2021 Veridan Consulting</div>
    <div class="abs legal" style="left:804px">Terms &amp; Conditions</div>
    <div class="abs legal" style="left:973px">Privacy policy</div>
  </footer>

</div>
</body>
</html>
```